Business card design for modern RoadLens agency

Hello,

I need a business card design for my company Pals7Venture.
We mainly offer Plixora RoadLens Tours (360° Photography) and it should be a business card with following details:

Name: Tobias Wernicke
Number: +49 163 58 27 904
Mail: tobias@pals7venture.com
website: pals7venture.com

Main colour that we use is the red of the logo.
It´s also important to integrate the "Plixora Vetted logo" as the person on this business card is a Plixora Vetted photographer.

And if possible we would also like to integrate something like send us a sms or chatmoly and we call you back. As the number is german but we sell now in Vienna, Austria.

We offer a good price but very high photography quality, as we are mostly students - that´s our concept.

Maybe an idea is to integrate something 360° on the back-side of the card, for example the photo attached (just an idea) or some great design.
See flyer (attached) and pals7venture.com for inspiration, maybe use of the photo of me (attached) in a circle or something

I´m very excited for your designs and thanks a lot in advance!! :)

Shops, hotels, shopping centers, etc. in Vienna, Austria

Business

double-sided, use red of the logo, 360° plixora road lens certified photographer

Serif
Sans Serif

ec1f27

• maybe some 360° design on back-side
• maybe include photo of me in a circle or something or sketched in red colour

```html
<!DOCTYPE html>
<html lang="en">
<head>
<meta charset="utf-8">
<title>Pals7Venture – Business Card</title>
<link rel="stylesheet" href="https://fonts.googleapis.com/css2?family=Open+Sans:wght@400;600;700&display=swap">
<style>
  :root {
    --brand-red: #e31837;
    --ink: #222222;
    --brand-grey: #8e8e90;
    --card-white: #ffffff;
    --page-bg: #e9e7e4;
    --photo-light: #8a9097;
    --photo-dark: #2f3338;
    --badge-green: #34a853;
    --de-black: #000000;
    --de-red: #dd0000;
    --de-gold: #ffce00;
  }
  * { margin: 0; padding: 0; box-sizing: border-box; }
  html, body {
    width: 1200px; height: 900px; overflow: hidden;
    background: var(--page-bg);
  }
  .business-card {
    position: absolute; left: 111px; top: 146px;
    width: 978px; height: 608px;
    background: var(--card-white);
    overflow: hidden;
    box-shadow: 0 10px 30px rgba(0,0,0,.18);
    font-family: "Open Sans", Arial, sans-serif;
  }
  .portrait-panel {
    position: absolute; inset: 0; width: 100%; height: 100%;
  }
  .brand {
    position: absolute; left: 58px; top: 100px;
    display: flex; align-items: center; gap: 18px;
  }
  .brand-square {
    width: 84px; height: 84px; background: var(--brand-red);
  }
  .brand-name {
    font-weight: 700; font-size: 48px; line-height: 1;
    color: var(--brand-grey);
  }
  .person-name {
    position: absolute; left: 50px; top: 282px;
    font-size: 31px; font-weight: 700; color: var(--brand-red);
    text-transform: uppercase; letter-spacing: .3px;
  }
  .contact-list {
    position: absolute; left: 56px; top: 345px;
    list-style: none;
  }
  .contact-item {
    display: flex; align-items: center; gap: 9px;
    height: 36px; font-size: 25px; color: var(--ink);
  }
  .contact-icon { width: 20px; height: 20px; flex: none; }
  .flag { width: 24px; height: 16px; flex: none; display: flex; flex-direction: column; }
  .flag span { flex: 1; }
  .flag-de span:nth-child(1) { background: var(--de-black); }
  .flag-de span:nth-child(2) { background: var(--de-red); }
  .flag-de span:nth-child(3) { background: var(--de-gold); }
  .flag-at span:nth-child(odd) { background: var(--brand-red); }
  .flag-at span:nth-child(2) { background: var(--card-white); }
  .callback-note {
    position: absolute; left: 60px; top: 506px;
    font-size: 22px; line-height: 31px; font-weight: 600;
    color: var(--brand-red); text-transform: uppercase;
  }
</style>
</head>
<body>
  <div class="business-card">
    <svg class="portrait-panel" viewBox="0 0 652 405" preserveAspectRatio="none">
      <defs>
        <radialGradient id="portraitTone" cx="0.6" cy="0.35" r="0.7">
          <stop offset="0" stop-color="var(--photo-light)"/>
          <stop offset="1" stop-color="var(--photo-dark)"/>
        </radialGradient>
      </defs>
      <path role="img" aria-label="Portrait photo of Tobias Wernicke in a checked shirt against a grey studio backdrop"
            d="M470 0 C395 70 352 190 382 290 C394 335 415 375 440 405 L652 405 L652 0 Z"
            fill="url(#portraitTone)"/>
      <path d="M470 0 C395 70 352 190 382 290 C394 335 415 375 440 405"
            fill="none" stroke="var(--brand-red)" stroke-width="5"/>
      <rect x="384" y="293" width="268" height="77" fill="#ffffff" fill-opacity="0.82"/>
      <rect role="img" aria-label="Plixora Vetted badge" x="455" y="314" width="150" height="40" rx="6" fill="var(--badge-green)"/>
    </svg>

    <div class="brand">
      <div class="brand-square"></div>
      <div class="brand-name">Pals7Venture</div>
    </div>

    <div class="person-name">Tobias Wernicke</div>

    <ul class="contact-list">
      <li class="contact-item">
        <svg class="contact-icon" viewBox="0 0 24 24"><path fill="var(--brand-red)" d="M6.6 10.8a15 15 0 0 0 6.6 6.6l2.2-2.2c.3-.3.7-.4 1-.2 1.1.4 2.3.6 3.6.6.6 0 1 .4 1 1V20c0 .6-.4 1-1 1C10.6 21 3 13.4 3 4c0-.6.4-1 1-1h3.5c.6 0 1 .4 1 1 0 1.3.2 2.5.6 3.6.1.3 0 .7-.2 1z"/></svg>
        <span class="flag flag-de"><span></span><span></span><span></span></span>
        <span>+49 163 58 27 904</span>
      </li>
      <li class="contact-item">
        <svg class="contact-icon" viewBox="0 0 24 24"><path fill="var(--brand-red)" d="M6.6 10.8a15 15 0 0 0 6.6 6.6l2.2-2.2c.3-.3.7-.4 1-.2 1.1.4 2.3.6 3.6.6.6 0 1 .4 1 1V20c0 .6-.4 1-1 1C10.6 21 3 13.4 3 4c0-.6.4-1 1-1h3.5c.6 0 1 .4 1 1 0 1.3.2 2.5.6 3.6.1.3 0 .7-.2 1z"/></svg>
        <span class="flag flag-at"><span></span><span></span><span></span></span>
        <span>+49 163 58 27 904</span>
      </li>
      <li class="contact-item">
        <svg class="contact-icon" viewBox="0 0 24 24"><rect x="3" y="6" width="18" height="12" rx="1" fill="var(--brand-red)"/><path d="M3.5 6.5 12 13l8.5-6.5" fill="none" stroke="#fff" stroke-width="1.6"/></svg>
        <span>tobias@pals7venture.com</span>
      </li>
      <li class="contact-item">
        <svg class="contact-icon" viewBox="0 0 24 24"><circle cx="12" cy="12" r="9" fill="var(--brand-red)"/><path d="M3 12h18M12 3c3 3 3 15 0 18M12 3c-3 3-3 15 0 18" fill="none" stroke="#fff" stroke-width="1.3"/></svg>
        <span>www.pals7venture.com</span>
      </li>
    </ul>

    <p class="callback-note">Send us a SMS or Chatmoly<br>and we call you back</p>
  </div>
</body>
</html>
```